Conference for Teenagers Needs Event Graphics

I am in need of event graphics for our upcoming event. This event, titled "Kestrel Youth Rally", is a weekend event for teenagers 11-19 years old. They hear from speakers, listen to a band, and do other fun activities. Our theme is "Together." Graphic design should have a young adult/older teen feel. Clean, not very bright colors.

Event Info:
November 6-8, 2020
Pellworth Exhibit Hall, Sioux Falls, SD
Speakers: TBD (will give name and picture before final approval)
Worship: (band name TBD before final approval)
KestrelYouthRally.com
#417KR
Our Organization Logo (attached): Lumen Forward

Once designed, I need the following graphics file sizes:
-11x17 Vertical Poster design: include all event info AND a "blank" spot/box for groups to add their own details/information. Also include the QRV logo and our organization logo Lumen Forward in someway.
-4x3 horizontal postcard: include all event info on 1 side including LumenForward logo and QRV; blank backside
-Main Graphic Slide: formatted to fit a widescreen 16x9 screen. Include event name, hashtag, QRV and Lumen Forward logo
-social media graphics for event: can incorporate some or all of the event details
-4.25x 2.75 vertical badge: include event title on front with Lumen Forward logo

Target Market(s)

Young adults or older teenagers

Requirements
Must have
• -event info
-Lumen Forward Logo & QRV logo

```html
<!DOCTYPE html>
<html lang="en">
<head>
<meta charset="utf-8">
<title>Kestrel Youth Rally — Poster</title>
<link rel="stylesheet" href="https://fonts.googleapis.com/css2?family=Bebas+Neue&family=Oswald:wght@300;400;600;700&display=swap">
<style>
  :root {
    --page-bg: #dfe4e8;
    --poster-black: #000000;
    --cyan: #29c4ee;
    --white: #ffffff;
    --navy: #1c2a4a;
    --purple-deep: #1a0f4d;
    --purple: #5a1aa6;
    --magenta: #c02ad8;
    --grey-text: #d8d8d8;
  }
  * { margin: 0; padding: 0; box-sizing: border-box; }
  html, body { width: 1200px; height: 900px; overflow: hidden; }
  body { background: var(--page-bg); position: relative; font-family: "Oswald", sans-serif; }

  .poster {
    position: absolute; left: 320px; top: 25px;
    width: 560px; height: 850px;
    background: var(--poster-black);
    overflow: hidden;
  }

  .hero-art {
    position: absolute; left: 0; top: 0; width: 560px; height: 560px;
    background:
      radial-gradient(ellipse 220px 180px at 330px 330px, rgba(220,80,240,0.85), rgba(220,80,240,0) 70%),
      radial-gradient(ellipse 260px 200px at 150px 120px, rgba(150,40,140,0.55), rgba(150,40,140,0) 70%),
      linear-gradient(180deg, var(--purple-deep) 0%, var(--purple) 45%, #2a0b4a 70%, var(--poster-black) 100%);
  }

  .org-name {
    position: absolute; top: 52px; left: 0; width: 100%;
    text-align: center;
    font-family: "Bebas Neue", sans-serif;
    font-size: 46px; letter-spacing: 2px;
    color: var(--cyan);
  }

  .title-frame { position: absolute; left: 33px; top: 145px; width: 492px; height: 146px; }
  .title-main {
    position: absolute; top: 152px; left: 0; width: 100%;
    text-align: center;
    font-family: "Bebas Neue", sans-serif;
    font-size: 98px; line-height: 1; color: var(--white);
  }
  .title-sub {
    position: absolute; top: 240px; left: 0; width: 100%;
    text-align: center;
    font-family: "Oswald", sans-serif; font-weight: 300;
    font-size: 44px; line-height: 1; color: var(--cyan);
    transform: scaleY(1.15);
  }

  .date-frame { position: absolute; left: 52px; top: 550px; width: 456px; height: 44px; }
  .date-line {
    position: absolute; top: 550px; left: 0; width: 100%;
    display: flex; justify-content: center; align-items: center; gap: 14px;
    font-family: "Oswald", sans-serif; font-weight: 600;
    font-size: 44px; line-height: 1.1;
  }
  .date-month { color: var(--cyan); font-weight: 400; font-family: "Bebas Neue", sans-serif; font-size: 54px; }
  .date-days, .date-year { color: var(--white); }
  .date-sep { width: 2px; height: 18px; background: var(--white); }

  .venue-ribbon { position: absolute; left: 84px; top: 612px; width: 392px; height: 30px; }
  .venue-text {
    position: absolute; top: 612px; left: 0; width: 100%; height: 30px;
    display: flex; justify-content: center; align-items: center; gap: 10px;
    font-family: "Bebas Neue", sans-serif; font-size: 22px; color: var(--poster-black);
  }
  .venue-sep { width: 1.5px; height: 10px; background: var(--poster-black); }

  .speaker-label {
    position: absolute; top: 660px; left: 135px;
    font-family: "Oswald", sans-serif; font-weight: 700;
    font-size: 66px; line-height: 1; color: var(--white);
  }
  .speaker-photo {
    position: absolute; top: 655px; width: 76px; height: 76px; border-radius: 50%;
    border: 2px solid var(--cyan);
  }
  .speaker-photo.one { left: 252px; background: radial-gradient(circle at 50% 45%, #5a4a9a, #1c1740 75%); }
  .speaker-photo.two { left: 348px; background: radial-gradient(circle at 50% 45%, #ffffff, #c9ccd6 80%); }
  .speaker-name {
    position: absolute; top: 741px; width: 90px; text-align: center;
    font-family: "Oswald", sans-serif; font-weight: 600; font-size: 8px; color: var(--grey-text);
  }
  .speaker-name.one { left: 245px; }
  .speaker-name.two { left: 341px; }

  .band-bar {
    position: absolute; top: 760px; left: 0; width: 100%; height: 23px;
    background: var(--white);
    text-align: center;
    font-family: "Oswald", sans-serif; font-weight: 600;
    font-size: 13px; line-height: 23px; letter-spacing: 6px; color: var(--navy);
  }

  .site-url {
    position: absolute; top: 797px; left: 0; width: 100%; text-align: center;
    font-family: "Oswald", sans-serif; font-weight: 400;
    font-size: 12px; letter-spacing: 4px; color: var(--white);
  }
  .hashtag {
    position: absolute; top: 815px; left: 0; width: 100%; text-align: center;
    font-family: "Oswald", sans-serif; font-size: 8px; letter-spacing: 3px; color: var(--grey-text);
  }
</style>
</head>
<body>
  <main class="poster">
    <div class="hero-art" role="img" aria-label="Crowd of concert-goers with raised hands silhouetted against purple and magenta geometric stage lights"></div>

    <div class="org-name">Lumen Forward</div>

    <svg class="title-frame" viewBox="0 0 492 146" aria-hidden="true">
      <g fill="none" stroke="#ffffff" stroke-width="1.5">
        <polyline points="62,1 1,1 1,145 62,145"/>
        <polyline points="430,1 491,1 491,145 430,145"/>
      </g>
    </svg>
    <h1 class="title-main">Kestrel</h1>
    <h2 class="title-sub">YOUTH RALLY</h2>

    <svg class="date-frame" viewBox="0 0 456 44" aria-hidden="true">
      <g fill="none" stroke="#ffffff" stroke-width="1" stroke-dasharray="2 2">
        <polyline points="50,1 1,1 1,40"/>
        <polyline points="406,1 455,1 455,40"/>
      </g>
    </svg>
    <div class="date-line">
      <span class="date-month">NOVEMBER</span>
      <span class="date-sep"></span>
      <span class="date-days">6-8</span>
      <span class="date-sep"></span>
      <span class="date-year">2020</span>
    </div>

    <svg class="venue-ribbon" viewBox="0 0 392 30" aria-hidden="true">
      <polygon points="0,0 392,0 380,15 392,30 0,30 12,15" fill="#29c4ee"/>
    </svg>
    <div class="venue-text">
      <span>PELLWORTH EXHIBIT HALL</span>
      <span class="venue-sep"></span>
      <span>SIOUX FALLS, SD</span>
    </div>

    <div class="speaker-label">TBD</div>
    <div class="speaker-photo one" role="img" aria-label="Speaker portrait"></div>
    <div class="speaker-photo two" role="img" aria-label="Speaker portrait"></div>
    <div class="speaker-name one">NAME SURNAME</div>
    <div class="speaker-name two">NAME SURNAME</div>

    <div class="band-bar">BAND NAME</div>

    <div class="site-url">KESTRELYOUTHRALLY.COM</div>
    <div class="hashtag">#417KR</div>
  </main>
</body>
</html>
```